Website for an AdOps/Media Agency

We need a logo for an ad operations firm. We help websites to maximize their advertising revenues by optimizing their ad networks, configurations, technologies, etc. The name is Brovilo, or BroVilo, to communicate that we take them to the top of their revenue potential. We want to also communicate, trust us to handle your adops, we take care of the hassle (it's an industry in continual technological innovation -- hard to stay on top of, and heavily manual, reporting, etc) and make sure our clients maximize ad revenues. For more info on site ideas/desires: https://files.quenmarto.com/doc/d/7XtRbnqLwe2Mz84PdkaHsYVoJcFuT3iGeZ5_rxOqNl/view?usp=sharing

Project Deadline Extended Reason: Apologies, I got caught up in other things. This is now priority, and will be guaranteed. I will also include an extra coding fee for a WP site and increase the budget. Thanks for your understanding! Added Thursday, July 7, 2016

Target Market(s)

Ad Operations/Media Consultancy

Industry/Entity Type

Ad Agency

Number of Pages Required

1 page

Font styles to use
Sans Serif

Requirements
Must have
• I like clean and simple, nice images, scrolling down.
Nice to have
• I like clean, fresh white running through the site. Note, I listed us as an ad agency, but only because there was no adops. We work with ad agencies, but we are more agents for publishers.
Should not have
• To much clutter.

```html
<!DOCTYPE html>
<html lang="en">
<head>
<meta charset="utf-8">
<title>Brovilo — Ad Operations</title>
<link rel="stylesheet" href="https://fonts.googleapis.com/css2?family=Open+Sans:wght@400;600;700&family=Raleway:wght@300;400&display=swap">
<style>
:root{
  --green:#4cb24a;
  --green-dark:#2f7d2e;
  --ink:#222;
  --muted:#444;
  --band:#ececec;
  --footer:#2a2a2a;
  --footer-light:#f4f4f4;
  --black:#0d0d0d;
  --white:#fff;
}
*{box-sizing:border-box;margin:0;padding:0}
html,body{width:1200px;height:3249px;overflow:hidden}
body{position:relative;background:var(--white);font-family:"Open Sans",Arial,sans-serif;color:var(--ink)}

.site-header{position:absolute;left:0;top:0;width:1200px;height:175px}
.brand{position:absolute;left:52px;top:58px;display:flex;align-items:center;gap:22px}
.brand-mark{width:66px;height:66px;border:4px solid var(--ink);border-radius:6px}
.brand-name{font-family:"Raleway",sans-serif;font-weight:400;font-size:50px;color:var(--green);letter-spacing:-1px}
.main-nav{position:absolute;right:52px;top:86px;display:flex;align-items:center;gap:30px;font-size:16px;font-weight:600;white-space:nowrap}
.main-nav a{color:var(--ink);text-decoration:none;padding-bottom:6px;border-bottom:4px solid transparent}
.main-nav a.active{border-bottom-color:var(--green)}
.main-nav a.cta{background:var(--green);color:var(--white);padding:10px 14px;border-radius:3px;border:0}

.hero{position:absolute;left:0;top:175px;width:1200px;height:550px}
.hero-photo{position:absolute;inset:0;background:linear-gradient(180deg,#b9d3e8 0%,#e6eef4 45%,#c9d3dc 70%,#f3f5f7 100%)}
.hero-copy{position:absolute;left:95px;top:170px;width:540px}
.hero-title{font-family:"Raleway",sans-serif;font-weight:300;font-size:48px;color:var(--ink);white-space:nowrap}
.hero-title span,.hero-text span{color:var(--green)}
.hero-text{font-size:20px;line-height:28px;color:var(--ink);margin-top:8px}
.btn{display:inline-block;background:var(--green);color:var(--white);font-size:20px;padding:5px 34px;margin-top:18px;border-radius:3px;text-decoration:none}
.hero-dots{position:absolute;left:574px;top:529px;display:flex;gap:9px}
.hero-dots i{width:9px;height:9px;border-radius:50%;background:#333}
.hero-dots i:first-child{background:#aaa}

.intro{position:absolute;left:0;top:725px;width:1200px;height:170px;background:var(--band);text-align:center;padding-top:30px}
.intro h2{font-size:30px;font-weight:400;color:var(--ink)}
.intro h2 strong{color:var(--green);font-weight:700}
.intro p{font-size:17px;line-height:25px;margin:14px auto 0;width:1010px}

.service{position:absolute;left:0;width:1200px;height:112px}
.service h3{font-size:18px;color:var(--green);font-weight:700;margin-bottom:2px;white-space:nowrap}
.service p{font-size:14px;line-height:20px;color:var(--ink)}
.icon{position:absolute;top:0;width:110px;height:110px;border-radius:50%;background:var(--white);box-shadow:0 0 0 2px #ddd;display:flex;align-items:center;justify-content:center}
.icon::before{content:"";position:absolute;inset:6px;border:6px solid var(--green);border-radius:50%}
.icon svg{width:50px;height:50px;position:relative}
.chev{position:absolute;top:42px;font-size:22px;line-height:22px;color:var(--ink)}
.service-text{position:absolute}

.subscribe{position:absolute;left:0;top:2800px;width:1200px;height:88px;background:var(--green)}
.subscribe h4{position:absolute;left:120px;top:26px;font-family:"Raleway",sans-serif;font-weight:300;font-size:28px;color:var(--white);white-space:nowrap}
.field{position:absolute;top:21px;height:46px;background:var(--green-dark);color:var(--white);font-size:14px;padding:13px 16px}
.subscribe .go{position:absolute;left:975px;top:21px;width:110px;height:46px;background:var(--black);color:var(--white);font-size:14px;font-weight:700;text-align:center;line-height:46px}

.site-footer{position:absolute;left:0;top:2888px;width:1200px;height:312px}
.site-footer > svg{position:absolute;inset:0}
.col{position:absolute;top:52px;color:var(--white)}
.col h5{font-size:16px;font-weight:700;padding-bottom:14px;border-bottom:1px solid #555;margin-bottom:20px}
.col li{list-style:none;font-size:14px;line-height:21px}
.contact li{display:flex;gap:14px;align-items:flex-start;margin-bottom:16px}
.contact svg{width:18px;height:18px;flex:none;margin-top:2px}
.msg-field{width:242px;height:32px;background:var(--black);font-size:12px;font-weight:700;padding:8px 10px;margin-bottom:4px}
.msg-field.tall{height:62px}
.submit{display:inline-block;background:var(--black);font-size:13px;font-weight:700;padding:6px 22px;margin-top:4px}
.footer-brand{position:absolute;left:860px;top:125px;display:flex;align-items:center;gap:22px}
.footer-brand .brand-mark{width:56px;height:56px}
.footer-brand .brand-name{font-size:44px}

.bottom-bar{position:absolute;left:0;top:3200px;width:1200px;height:49px;background:var(--black);color:var(--white);font-size:12px;font-weight:700;padding:17px 0 0 46px}
.social{position:absolute;right:46px;top:14px;display:flex;gap:8px}
.social i{width:22px;height:22px;border-radius:50%;background:var(--white)}
</style>
</head>
<body>

<header class="site-header">
  <div class="brand"><div class="brand-mark"></div><span class="brand-name">brovilo</span></div>
  <nav class="main-nav">
    <a class="active">Home</a><a>About</a><a>Publisher</a><a>Advertiser</a><a>Contact</a><a class="cta">Request a Consult</a>
  </nav>
</header>

<section class="hero">
  <div class="hero-photo" role="img" aria-label="Mountaineer with backpack standing on a snowy mountain ridge under a cloudy sky"></div>
  <div class="hero-copy">
    <h1 class="hero-title">Welcome to <span>brovilo</span></h1>
    <p class="hero-text"><span>brovilo</span> help websites to maximize their advertising revenues by optimizing their ad networks, configurations, technologies, etc.</p>
    <a class="btn">Learn More</a>
  </div>
  <div class="hero-dots"><i></i><i></i><i></i><i></i></div>
</section>

<section class="intro">
  <h2><strong>One-stop shop</strong> for all your monetization needs</h2>
  <p>Let our team join your team to Optimize your adops and maximize your monetization Leave it to us to streamline, optimize, and manage your ad network relationships and operations: We'll take your revenues to the top.</p>
</section>

<div class="service" style="top:960px">
  <div class="icon" style="left:103px"><svg viewBox="0 0 50 50" fill="#222"><rect x="6" y="34" width="6" height="10"/><rect x="15" y="28" width="6" height="16"/><rect x="24" y="22" width="6" height="22"/><rect x="33" y="16" width="6" height="28"/><text x="6" y="20" font-size="18" font-weight="700" font-family="Open Sans, sans-serif">$</text></svg></div>
  <span class="chev" style="left:224px">›</span>
  <div class="service-text" style="left:249px;top:22px;width:880px"><h3>Monetization Strategy &amp; Planning:</h3><p>There's no "one size fits all" ads strategy.  We help you find the winning combination, placements and mix for your adspace offer.</p></div>
</div>

<div class="service" style="top:1092px">
  <div class="icon" style="left:989px"><svg viewBox="0 0 50 50" fill="none" stroke="#222" stroke-width="3"><rect x="6" y="8" width="34" height="30" rx="3"/><line x1="6" y1="16" x2="40" y2="16"/><circle cx="36" cy="36" r="8" fill="#fff"/></svg></div>
  <span class="chev" style="left:962px">‹</span>
  <div class="service-text" style="left:123px;top:24px;width:825px"><h3>Network Configurations:</h3><p>From header bidders, to video, to native, to display, we create your optimum mix for maximum monetization: Screening, implementation, testing, measurement, and ongoing optimization to keep revenues at a max.</p></div>
</div>

<div class="service" style="top:1238px">
  <div class="icon" style="left:103px"><svg viewBox="0 0 50 50" fill="none" stroke="#222" stroke-width="4"><circle cx="20" cy="25" r="12"/><circle cx="30" cy="25" r="12"/></svg></div>
  <span class="chev" style="left:224px">›</span>
  <div class="service-text" style="left:249px;top:24px;width:880px"><h3>Access to Premium Pexora Adex Account:</h3><p>Get the same rates as the big guys, with individualized, ongoing Adex optimization in our Pexora partner account, including access to our select premium marketplace deals.</p></div>
</div>

<div class="service" style="top:1380px">
  <div class="icon" style="left:989px"><svg viewBox="0 0 50 50" fill="none" stroke="#222" stroke-width="3" stroke-linejoin="round"><path d="M4 20l10-6 10 6 8-5 14 8M14 30l8 7c2 2 5 0 3-2M20 27l8 7c2 2 5 0 3-2M25 24l7 6c2 2 5 0 3-2l-10-8"/></svg></div>
  <span class="chev" style="left:962px">‹</span>
  <div class="service-text" style="left:167px;top:24px;width:780px"><h3>Contract Negotiation &amp; Relationship Management:</h3><p>We help to make sure you are getting the best possible pricing and terms, and keep the relations to make sure the premium offers keep coming your way.</p></div>
</div>

<div class="service" style="top:1520px">
  <div class="icon" style="left:103px"><svg viewBox="0 0 50 50" fill="#222"><ellipse cx="20" cy="10" rx="14" ry="5"/><rect x="6" y="14" width="28" height="8" rx="3"/><rect x="6" y="25" width="28" height="8" rx="3"/><rect x="6" y="36" width="22" height="8" rx="3"/><circle cx="38" cy="38" r="8" fill="none" stroke="#222" stroke-width="4"/></svg></div>
  <span class="chev" style="left:224px">›</span>
  <div class="service-text" style="left:249px;top:32px;width:880px"><h3>Ad server set-up, training &amp; troubleshooting:</h3><p>Header Bidding, Video, Native, Display…we stay on top of the technologies, so you don't have to.</p></div>
</div>

<div class="service" style="top:1660px">
  <div class="icon" style="left:989px"><svg viewBox="0 0 50 50" fill="none" stroke="#222" stroke-width="2.5"><path d="M4 36h42M6 34l10-10 8 6 10-12 10 8"/><circle cx="34" cy="16" r="5"/></svg></div>
  <span class="chev" style="left:962px">‹</span>
  <div class="service-text" style="left:314px;top:32px;width:640px"><h3>Ad tag implementation &amp; tracking:</h3><p>Let us take care of the details: orders, CPMs, scheduling, targeting, volumes, frequency caps.</p></div>
</div>

<div class="service" style="top:1800px">
  <div class="icon" style="left:103px"><svg viewBox="0 0 50 50" fill="#222"><rect x="6" y="30" width="6" height="14"/><rect x="15" y="24" width="6" height="20"/><rect x="24" y="16" width="6" height="28"/><rect x="33" y="6" width="8" height="38"/></svg></div>
  <span class="chev" style="left:224px">›</span>
  <div class="service-text" style="left:249px;top:32px;width:880px"><h3>Propriety Campaign Performance &amp; Reporting Tools:</h3><p>Daily reporting, continuous monitoring for performance, discrepancies, and optimization.</p></div>
</div>

<div class="service" style="top:1938px">
  <div class="icon" style="left:989px"><svg viewBox="0 0 50 50" fill="none" stroke="#222" stroke-width="3"><rect x="6" y="10" width="38" height="30" rx="3"/><line x1="12" y1="18" x2="38" y2="18"/><line x1="12" y1="25" x2="38" y2="25"/><line x1="12" y1="32" x2="30" y2="32"/></svg></div>
  <span class="chev" style="left:962px">‹</span>
  <div class="service-text" style="left:548px;top:32px;width:405px"><h3>Propriety Header Bidder Implementation:</h3><p>Propriety Header Bidder Implementation:</p></div>
</div>

<div class="service" style="top:2080px">
  <div class="icon" style="left:103px"><svg viewBox="0 0 50 50" fill="#222"><circle cx="25" cy="14" r="9" fill="none" stroke="#222" stroke-width="3"/><circle cx="25" cy="14" r="3"/><circle cx="12" cy="32" r="5"/><circle cx="38" cy="32" r="5"/><circle cx="25" cy="30" r="6"/><path d="M4 46c0-8 16-8 16 0zM30 46c0-8 16-8 16 0zM15 46c0-9 20-9 20 0z"/></svg></div>
  <span class="chev" style="left:224px">›</span>
  <div class="service-text" style="left:249px;top:32px;width:880px"><h3>Audience Segmentation, Targeting &amp; Marketing:</h3><p>Target, segment, package &amp; sell your audiences to the right advertisers for maximum revenues.</p></div>
</div>

<div class="service" style="top:2220px">
  <div class="icon" style="left:989px"><svg viewBox="0 0 50 50" fill="#222"><circle cx="18" cy="20" r="11"/><circle cx="18" cy="20" r="4" fill="#fff"/><circle cx="36" cy="36" r="8"/><circle cx="36" cy="36" r="3" fill="#fff"/></svg></div>
  <span class="chev" style="left:962px">‹</span>
  <div class="service-text" style="left:162px;top:24px;width:790px"><h3>Ongoing Optimization:</h3><p>The Holy Grail.  We never stop tweaking and tightening to keep your revenues optimized and adjusted for seasonal fluctuations.</p></div>
</div>

<div class="service" style="top:2360px">
  <div class="icon" style="left:103px"><svg viewBox="0 0 50 50" fill="none" stroke="#222" stroke-width="3"><rect x="8" y="6" width="32" height="38" rx="2"/><path d="M14 16l3 3 5-6M14 28l3 3 5-6"/><line x1="26" y1="16" x2="35" y2="16"/><line x1="26" y1="28" x2="35" y2="28"/></svg></div>
  <span class="chev" style="left:224px">›</span>
  <div class="service-text" style="left:249px;top:32px;width:880px"><h3>Quality Control:</h3><p>We work with you to keep bad ads out, and block lists up-to-date.</p></div>
</div>

<div class="service" style="top:2500px">
  <div class="icon" style="left:989px"><svg viewBox="0 0 50 50" fill="#222"><rect x="10" y="6" width="3" height="38"/><rect x="23" y="6" width="3" height="38"/><rect x="36" y="6" width="3" height="38"/><rect x="6" y="28" width="11" height="8" rx="2"/><rect x="19" y="12" width="11" height="8" rx="2"/><rect x="32" y="22" width="11" height="8" rx="2"/></svg></div>
  <span class="chev" style="left:962px">‹</span>
  <div class="service-text" style="left:487px;top:32px;width:470px"><h3>Direct Advertiser Management:</h3><p>We field &amp; manage your direct advertiser enquiries and campaigns.</p></div>
</div>

<div class="service" style="top:2640px">
  <div class="icon" style="left:103px"><svg viewBox="0 0 50 50" fill="none" stroke="#222" stroke-width="2.5"><path d="M25 6a12 12 0 0 0-7 22v6h14v-6a12 12 0 0 0-7-22z"/><line x1="19" y1="38" x2="31" y2="38"/><line x1="21" y1="42" x2="29" y2="42"/></svg></div>
  <span class="chev" style="left:224px">›</span>
  <div class="service-text" style="left:249px;top:32px;width:880px"><h3>Business Development:</h3><p>We stay on top of the latest trends and best technologies, so you don't have to!</p></div>
</div>

<section class="subscribe">
  <h4>Subscribe to our mailing list</h4>
  <div class="field" style="left:496px;width:230px">Name</div>
  <div class="field" style="left:736px;width:228px">Email</div>
  <div class="go">SUBSCRIBE</div>
</section>

<footer class="site-footer">
  <svg viewBox="0 0 1200 312" preserveAspectRatio="none"><rect width="1200" height="312" fill="#2a2a2a"/><polygon points="920,0 1200,0 1200,312 780,312" fill="#f4f4f4"/></svg>
  <div class="col" style="left:76px;width:150px">
    <h5>QUICK LINKS</h5>
    <ul><li>HOME</li><li>ABOUT</li><li>PUBLISHER</li><li>ADVERTISER</li><li>CONTACT</li><li>REQUEST A CONSULT</li></ul>
  </div>
  <div class="col contact" style="left:280px;width:200px">
    <h5>CONTACT US</h5>
    <ul>
      <li><svg viewBox="0 0 20 20" fill="#fff"><path d="M10 1a6 6 0 0 0-6 6c0 5 6 12 6 12s6-7 6-12a6 6 0 0 0-6-6zm0 8a2 2 0 1 1 0-4 2 2 0 0 1 0 4z"/></svg><span>48 Ridgeway Ln<br>Marrowfield, CA 90417</span></li>
      <li><svg viewBox="0 0 20 20" fill="#fff"><path d="M5 2l3 4-2 2c1 3 3 5 6 6l2-2 4 3-2 3C9 18 2 11 2 4z"/></svg><span>555.014.2290</span></li>
      <li><svg viewBox="0 0 20 20" fill="none" stroke="#fff" stroke-width="2"><rect x="2" y="4" width="16" height="12"/><path d="M2 4l8 7 8-7"/></svg><span>info@brovilo.com</span></li>
    </ul>
  </div>
  <div class="col" style="left:514px;width:245px">
    <h5>SEND A MESSAGE</h5>
    <div class="msg-field">Name</div>
    <div class="msg-field">Email</div>
    <div class="msg-field tall">Message</div>
    <div class="submit">SUBMIT</div>
  </div>
  <div class="footer-brand"><div class="brand-mark"></div><span class="brand-name">brovilo</span></div>
</footer>

<div class="bottom-bar">COPYRIGHT © 2016 BROVILO. ALL RIGHTS RESERVED.
  <div class="social"><i></i><i></i><i></i></div>
</div>

</body>
</html>
```